Tobin's Jewelry Studio Needs a Moving Location Flyer

We need a flyer to inform our customers of our location moving. We will be moving to our city's downtown which is only 1 mile away from our current address. We will be having a moving sale ( Up to 80% off). The sale starts Sept. 8th Our business creates, sells, and repairs fine jewelry. Dimensions are 5"x8"

Target Market(s)

Women ages 25-55

Industry/Entity Type

Jewelry

Colors
85abd2
cfdeed

Requirements
Must have
• Our logo
• Mention of the sale
• Our current address
• 4187 Marsh Creek Blvd.
• Brookhollow, Ca 91642
• (909)417-2863
Nice to have
• Mention that we're relocating to downtown Brookhollow (new location opening Nov. 1st.)

```html
<!DOCTYPE html>
<html lang="en">
<head>
<meta charset="utf-8">
<title>Tobin's Jewelry Studio – Moving Sale Flyer</title>
<link rel="stylesheet" href="https://fonts.googleapis.com/css2?family=Arvo:wght@400;700&family=Comfortaa:wght@300&family=Zilla+Slab:wght@300;400&display=swap">
<style>
  :root {
    --page-bg: #e6e5e2;
    --paper: #ffffff;
    --teal: #6ec3cc;
    --teal-soft: #a9dde3;
    --periwinkle: #7b95d6;
    --brand-blue: #85abd2;
    --brand-blue-pale: #cfdeed;
    --deep-blue: #6f8fd0;
    --brown: #5a3426;
  }
  * { margin: 0; padding: 0; box-sizing: border-box; }
  html, body { width: 1200px; height: 1200px; overflow: hidden; }
  body { background: var(--page-bg); position: relative; }

  .flyer {
    position: absolute;
    left: 250px; top: 40px;
    width: 700px; height: 1120px;
    background: linear-gradient(to bottom, var(--paper) 0%, var(--paper) 72%, var(--brand-blue-pale) 84%, var(--deep-blue) 100%);
    overflow: hidden;
    box-shadow: 0 6px 18px rgba(0,0,0,0.12);
  }

  .brand {
    position: absolute; top: 56px; left: 0; right: 0;
    display: flex; align-items: center; justify-content: center; gap: 14px;
  }
  .brand-rule { width: 70px; height: 3px; background: var(--brown); }
  .brand-dot { width: 46px; height: 46px; border-radius: 50%; background: var(--teal-soft); }
  .brand-name {
    font-family: "Arvo", serif; font-weight: 700; font-size: 26px;
    color: var(--brown); letter-spacing: 0.5px;
  }

  .headline {
    position: absolute; top: 150px; left: 0; right: 0;
    text-align: center;
    font-family: "Arvo", serif; font-weight: 700; font-size: 42px; line-height: 1.1;
    color: var(--teal);
  }

  .ring-photo {
    position: absolute; top: 268px; left: 30px; right: 30px; height: 290px;
    background: radial-gradient(ellipse at 50% 55%, #eef8f9 0%, #cfe7ea 45%, #9fc9cf 100%);
    border-radius: 6px;
  }

  .sale-line {
    position: absolute; left: 0; right: 40px; top: 584px;
    text-align: right;
    font-family: "Zilla Slab", serif; font-weight: 300; font-size: 50px; line-height: 1.0;
    color: var(--periwinkle);
  }

  .up-to {
    position: absolute; left: 40px; top: 810px;
    font-family: "Zilla Slab", serif; font-weight: 400; font-size: 48px; line-height: 1;
    color: var(--teal-soft);
  }

  .big-number {
    position: absolute; left: 160px; top: 700px;
    width: 420px; height: 280px;
  }
  .big-number text {
    font-family: "Comfortaa", sans-serif; font-weight: 300; font-size: 320px;
    fill: var(--teal); letter-spacing: -10px;
  }

  .percent {
    position: absolute; left: 585px; top: 715px;
    font-family: "Zilla Slab", serif; font-weight: 300; font-size: 64px; line-height: 1;
    color: var(--teal-soft);
  }
  .percent-off {
    position: absolute; left: 585px; top: 790px;
    font-family: "Zilla Slab", serif; font-weight: 300; font-size: 54px; line-height: 1;
    color: var(--teal-soft);
  }

  .contact {
    position: absolute; left: 0; right: 0; top: 1010px;
    text-align: center;
    font-family: "Arvo", serif; font-weight: 400; font-size: 20px; letter-spacing: 1px;
    color: #ffffff; line-height: 1.6; white-space: nowrap;
  }
</style>
</head>
<body>
  <main class="flyer">
    <header class="brand">
      <span class="brand-rule"></span>
      <span class="brand-dot"></span>
      <span class="brand-name">Tobin's jewelry studio</span>
      <span class="brand-rule"></span>
    </header>

    <h1 class="headline">on November 1st<br>we're heading downtown</h1>

    <div class="ring-photo" role="img" aria-label="Photograph of diamond halo engagement rings in white gold"></div>

    <p class="sale-line">moving sale<br>from September 8th</p>

    <p class="up-to">up to</p>
    <svg class="big-number" viewBox="0 0 420 280" aria-label="80">
      <text x="210" y="262" text-anchor="middle">80</text>
    </svg>
    <p class="percent">%</p>
    <p class="percent-off">off</p>

    <address class="contact" style="font-style: normal;">
      <p>4187 Marsh Creek Blvd, Brookhollow, Ca 91642</p>
      <p>(909) 417-2863</p>
    </address>
  </main>
</body>
</html>
```